Web Design Templates for redesigning the existing website

We need TWO coded web design templates (html+css format), i.e. one for the Top page and the other for the Content page, for redesigning our current website (http://www.kobu-lens.com/), which is a BtoC Japanese patent information service via email publishing.
Proposed templates must be:
1) Fully responsive
like this template -> http://trial-qx.net/mzt417/
Fine view must be kept on any device (PC, tablet, smartphone, etc.) with the latest version of any browser (IE, Firefox, Chrome, Safari, etc.).
Especially, we put the importance on how good it looks on a smartphone display.
2) Non wordpress template
You may use any wordpress templates as a reference.
However, proposed templates must NOT be a wordpress template.
3) Design taste = flat and simple
like the websites of PixelHerd, eBench, etc.
4) Colors (or color taste) based on the current website
THAT brown and THAT red have to be used as the basis.
5) Fully compatible for the double-byte character
Remember this is a Japanese site.
It is more preferably if you can also propose a Japanese font to be used on your proposed templates.
6) Entry field
We want to move the current entry field on http://www.kobu-lens.com/navi/navi_search to the redesigned Top page.
Accordingly, your proposed Top page template must include it.
7) Need NOT include contents (text, photo, etc.)
We now want just templates.
BtoC
Japanese engi

```html
<!DOCTYPE html>
<html lang="en">
<head>
<meta charset="utf-8">
<title>Kobu Lens</title>
<link rel="stylesheet" href="https://fonts.googleapis.com/css2?family=PT+Sans+Narrow:wght@400;700&family=Source+Sans+3:ital,wght@0,400;0,600;1,400&family=Noto+Sans+JP:wght@400&display=swap">
<style>
:root{
  --red:#b01b26;
  --red-dark:#a3151f;
  --tile:#e6e6e6;
  --ink:#4d4d4d;
  --ink-soft:#666;
  --line:#c9c9c9;
  --white:#fff;
}
*{box-sizing:border-box;margin:0;padding:0}
html,body{width:1200px;height:979px;overflow:hidden;background:var(--white)}
body{position:relative;font-family:"Source Sans 3",sans-serif;color:var(--ink)}
.page{position:absolute;left:181px;top:0;width:840px;height:979px}

.brand{position:absolute;left:0;top:30px;display:flex;align-items:center;gap:8px}
.brand-mark{width:34px;height:34px;background:var(--red)}
.brand-name{font-weight:600;font-size:38px;line-height:50px;color:var(--red);letter-spacing:-0.5px}
.tagline{position:absolute;left:218px;top:46px;font-family:"Noto Sans JP",sans-serif;font-size:11px;color:var(--ink)}

.search{position:absolute;left:624px;top:56px;width:214px;height:22px;border:1px solid var(--line);display:flex;align-items:center;padding:0 10px;font-size:9px;color:var(--ink-soft)}
.search svg{position:absolute;right:8px;top:4px}

.main-nav{position:absolute;left:0;top:104px;width:840px;height:39px;background:linear-gradient(#d2565f,var(--red) 60%,var(--red-dark));font-family:"PT Sans Narrow",sans-serif;font-size:12px;color:var(--white)}
.main-nav .current{position:absolute;left:0;top:0;width:95px;height:39px;background:linear-gradient(#c7424c,#a1141e)}
.main-nav a{position:absolute;top:12px;color:var(--white);text-decoration:none;white-space:nowrap}

.hero{position:absolute;left:0;top:143px;width:840px;height:431px;background:linear-gradient(100deg,#e9e6e1 0%,#f4f2ee 30%,#d8d0c6 55%,#ece8e2 75%,#c9bfb2 100%)}
.news-arrows{position:absolute;right:0;top:339px;width:43px;height:21px;background:rgba(70,70,70,.8);display:flex;justify-content:space-around;align-items:center}
.news-bar{position:absolute;left:0;top:360px;width:840px;height:71px;background:rgba(70,70,70,.78);color:var(--white)}
.news-label{position:absolute;left:27px;top:26px;font-size:16px}
.news-bar .rule{position:absolute;left:142px;top:10px;width:1px;height:61px;background:rgba(255,255,255,.6)}
.news-date{position:absolute;left:161px;top:13px;font-size:10px}
.news-text{position:absolute;left:161px;top:30px;width:660px;font-size:10px;line-height:15px}

.services{position:absolute;left:0;top:581px;width:840px;height:147px;display:flex;gap:7px}
.service{flex:1;background:var(--tile);color:var(--ink);text-align:center;font-size:15px;line-height:23px;padding-top:20px}
.service svg{display:block;margin:0 auto 14px}
.service.is-active{background:var(--red);color:var(--white)}

.welcome{position:absolute;left:0;top:753px;width:840px}
.welcome h1{font-size:13px;font-weight:600;color:var(--red);margin-bottom:8px;padding-left:1px}
.welcome p{font-size:9px;line-height:15.5px;color:var(--ink-soft)}

.feed{position:absolute;left:0;top:849px;width:840px;height:45px;background:var(--tile)}
.feed-name{position:absolute;left:0;top:0;width:141px;height:45px;border-right:1px solid var(--white);display:flex;align-items:center;justify-content:center;font-size:18px;font-weight:600;color:#8a8a8a}
.feed-text{position:absolute;left:158px;top:15px;font-size:10px;font-style:italic;color:var(--ink-soft)}
.feed-text a{color:var(--red);text-decoration:none}

.footer-nav{position:absolute;left:4px;top:915px;font-size:8.5px;color:var(--ink);display:flex;gap:15px}
.copyright{position:absolute;left:4px;top:935px;font-size:8.5px;color:var(--ink)}
.follow{position:absolute;right:3px;top:915px;display:flex;align-items:center;gap:4px;font-size:8px}
.follow span.dot{width:26px;height:26px;border-radius:50%;display:block}
</style>
</head>
<body>
<div class="page">
  <header>
    <div class="brand"><span class="brand-mark"></span><span class="brand-name">Kobu Lens</span></div>
    <div class="tagline">イノベーションを支える新しいメディア</div>
    <div class="search">SEARCH :
      <svg width="14" height="12" viewBox="0 0 14 12"><circle cx="5" cy="5" r="3.5" fill="none" stroke="#bbb" stroke-width="1.5"/><line x1="7.5" y1="7.5" x2="12" y2="11" stroke="#bbb" stroke-width="2"/></svg>
    </div>
  </header>

  <nav class="main-nav">
    <span class="current"></span>
    <a style="left:35px">HOME</a>
    <a style="left:117px">ADVERTISE</a>
    <a style="left:218px">TO ENGINEERS WHO TREND OF CONFLICT IS A CONCERN</a>
    <a style="left:516px">FOR A COMPANIES THAT HOLD PATENT RIGHTS</a>
    <a style="left:774px">FAQ</a>
  </nav>

  <section class="hero" role="img" aria-label="Photo of business people smiling in a bright meeting room with laptops">
    <div class="news-arrows">
      <svg width="6" height="8" viewBox="0 0 6 8"><path d="M5 0 1 4l4 4" fill="none" stroke="#fff"/></svg>
      <svg width="6" height="8" viewBox="0 0 6 8"><path d="M1 0l4 4-4 4" fill="none" stroke="#fff"/></svg>
    </div>
    <div class="news-bar">
      <div class="news-label">LATEST NEWS :</div>
      <span class="rule"></span>
      <div class="news-date">13 SEP 2013</div>
      <div class="news-text">it has a more-or-less normal distribution of letters, as opposed to using 'Content here, content here', making it look like readable English. Many desktop publishing packages and web page editors now use Lorem Ipsum as their default modell...</div>
    </div>
  </section>

  <section class="services">
    <div class="service is-active">
      <svg width="50" height="54" viewBox="0 0 50 54"><circle cx="30" cy="20" r="15" fill="none" stroke="#fff" stroke-width="6"/><line x1="19" y1="31" x2="5" y2="49" stroke="#fff" stroke-width="7" stroke-linecap="round"/></svg>
      ORIGINAL<br>SEARCH ENGINE
    </div>
    <div class="service">
      <svg width="40" height="54" viewBox="0 0 40 54"><path d="M12 52C2 40 6 22 22 18V8l16 16-16 16V30C12 30 8 40 12 52Z" fill="#777"/></svg>
      IPC<br>SUBCLASS DIRECT INPUT
    </div>
    <div class="service">
      <svg width="58" height="54" viewBox="0 0 58 54"><circle cx="19" cy="16" r="10" fill="#777"/><circle cx="39" cy="16" r="10" fill="#777"/><path d="M2 44c0-12 8-18 17-18s17 6 17 18Z" fill="#777"/><path d="M22 44c0-12 8-18 17-18s17 6 17 18Z" fill="#777"/><circle cx="29" cy="26" r="11" fill="#777" stroke="#e6e6e6" stroke-width="3"/><path d="M12 54c0-12 8-17 17-17s17 5 17 17Z" fill="#777" stroke="#e6e6e6" stroke-width="3"/></svg>
      PATENT<br>HOLDER FOR SERVICE
    </div>
    <div class="service">
      <svg width="54" height="54" viewBox="0 0 54 54"><rect x="1" y="13" width="52" height="34" rx="3" fill="#777"/><path d="M3 15l24 18 24-18M3 45l18-14M51 45 33 31" fill="none" stroke="#e6e6e6" stroke-width="2"/></svg>
      ADVERTISING TO<br>E-MAIL MAGAZINE
    </div>
  </section>

  <section class="welcome">
    <h1>WELCOME TO KOBU LENS</h1>
    <p>It is a long established fact that a reader will be distracted by the readable content of a page when looking at its layout. The point of using Lorem Ipsum is that it has a more-or-less normal distribution of letters, as opposed to using 'Content here, content here', making it look like readable English. Many desktop publishing packages and web page editors now use Lorem Ipsum as their default model text, and a search for 'lorem ipsum' will uncover many web sites still in their infancy. Various versions have evolved over the years, sometimes by accident, sometimes on purpose</p>
  </section>

  <section class="feed">
    <div class="feed-name">Chirpline</div>
    <p class="feed-text">It is a long established fact that a reader will be distracted by the readable content of a page when looking at its layout. <a href="#">www.plainwire.com</a></p>
  </section>

  <footer>
    <div class="footer-nav"><span>HOME</span><span>|</span><span>ADVERTISE</span><span>|</span><span>TO ENGINEERS WHO TREND OF CONFLICT IS A CONCERN</span><span>|</span><span>FOR A COMPANIES THAT HOLD PATENT RIGHTS</span><span>|</span><span>FAQ</span></div>
    <div class="copyright">COPYRIGHTS @2013.&nbsp; KOBU LENS ALL RIGHTS RESERVED</div>
    <div class="follow">FOLLOW US :
      <span class="dot" style="background:#2f5fa8" aria-label="Circlebook"></span>
      <span class="dot" style="background:#3aaee0" aria-label="Chirpline"></span>
      <span class="dot" style="background:#1c7fa6" aria-label="Linkhall"></span>
    </div>
  </footer>
</div>
</body>
</html>
```